I'm an electrician and the name of my company is called Brisk 'N' Bright Electrical. I require a professional business card that speaks to my clients, I also need it to be innovative and modern. We do maintenance & service work for domestic and commercial premises.

Industry/Entity Type

Electrical

Contact Information for Business Card

Must have the name of my company Brisk 'N' Bright Electrical, my name Darren Kolovich and my contact details 0427 318 592 and company email address Brisknbrightelectrical@quillpost.example and/or website Brisknbrightelectrical.example.au

Logo Text

Brisk 'N' Bright Electrical (If possible)

Colors
33a6d7
0592cd
3176b5

```html
<!DOCTYPE html>
<html lang="en">
<head>
<meta charset="utf-8">
<title>Brisk 'N' Bright Electrical — Business Card</title>
<link rel="stylesheet" href="https://fonts.googleapis.com/css2?family=Montserrat:wght@400;500;700;800&display=swap">
<style>
  :root {
    --backdrop: #1f1f21;
    --card: #ffffff;
    --ink: #111111;
    --accent-red: #d71f26;
    --brand-blue: #0592cd;
    --brand-sky: #33a6d7;
    --brand-navy: #3176b5;
    --rule: #c9c9c9;
    --text: #222222;
  }
  * { margin: 0; padding: 0; box-sizing: border-box; }
  html, body {
    width: 1200px; height: 1015px; overflow: hidden;
    background: var(--backdrop);
    font-family: "Montserrat", sans-serif;
  }
  .canvas {
    position: relative; width: 1200px; height: 1015px;
    display: flex; flex-direction: column; align-items: center;
    justify-content: center; gap: 40px;
  }
  .card {
    position: relative;
    width: 800px; height: 457px;
    background: var(--card);
    border-radius: 22px;
    box-shadow: 0 14px 30px rgba(0,0,0,.55);
    overflow: hidden;
  }
  .brand {
    display: flex; align-items: center; gap: 14px;
    color: var(--ink);
  }
  .brand-dot {
    flex: none; width: 30px; height: 30px; border-radius: 50%;
    background: var(--accent-red);
  }
  .brand-name {
    font-weight: 800; line-height: 1.05; font-size: 34px;
    letter-spacing: .2px;
  }
  .card-front .brand {
    position: absolute; left: 50%; top: 50%;
    transform: translate(-50%, -50%);
  }
  .card-front .brand-dot { width: 40px; height: 40px; }
  .card-front .brand-name { font-size: 44px; }

  .card-back .brand {
    position: absolute; right: 48px; top: 44px;
  }
  .card-back .brand-name { font-size: 28px; }

  .contact-block {
    position: absolute; left: 60px; bottom: 58px;
  }
  .person-row {
    display: flex; align-items: center; gap: 14px;
    margin-bottom: 14px;
  }
  .person-name {
    color: var(--brand-blue); font-weight: 700;
    font-size: 30px; letter-spacing: 1px; text-transform: uppercase;
    white-space: nowrap;
  }
  .person-rule {
    width: 370px; height: 1px; background: var(--rule);
  }
  .contact-list { list-style: none; }
  .contact-list li {
    display: flex; align-items: center; gap: 14px;
    font-size: 17px; color: var(--text); font-weight: 500;
    margin-top: 10px;
  }
  .contact-list svg {
    width: 24px; height: 24px; flex: none;
    stroke: var(--brand-navy); fill: none; stroke-width: 1.6;
    stroke-linecap: round; stroke-linejoin: round;
  }
</style>
</head>
<body>
<main class="canvas">

  <section class="card card-front" aria-label="Card front">
    <div class="brand">
      <span class="brand-dot"></span>
      <span class="brand-name">Brisk 'N' Bright<br>Electrical</span>
    </div>
  </section>

  <section class="card card-back" aria-label="Card back">
    <div class="brand">
      <span class="brand-dot"></span>
      <span class="brand-name">Brisk 'N' Bright<br>Electrical</span>
    </div>

    <div class="contact-block">
      <div class="person-row">
        <h1 class="person-name">Darren Kolovich</h1>
        <span class="person-rule"></span>
      </div>
      <ul class="contact-list">
        <li>
          <svg viewBox="0 0 24 24" aria-hidden="true"><rect x="2" y="2" width="20" height="20" rx="5"/><path d="M8 6.5l2 2.2-1.2 1.6c.9 1.8 2.3 3.2 4.1 4.1l1.6-1.2 2.2 2-1.4 2c-4.6-.6-8.2-4.2-8.8-8.8z"/></svg>
          0427 318 592
        </li>
        <li>
          <svg viewBox="0 0 24 24" aria-hidden="true"><rect x="2.5" y="5" width="19" height="14" rx="1.5"/><path d="M3 6l9 7 9-7"/></svg>
          Brisknbrightelectrical@quillpost.example
        </li>
        <li>
          <svg viewBox="0 0 24 24" aria-hidden="true"><circle cx="12" cy="12" r="9.5"/><path d="M2.5 12h19M12 2.5c3 3 3 16 0 19M12 2.5c-3 3-3 16 0 19"/></svg>
          Brisknbrightelectrical.example.au
        </li>
      </ul>
    </div>
  </section>

</main>
</body>
</html>
```